Postcard Design Project

private loan company where loans are funded by private individual investors.
This would be a postcard advertising for additional investors.

```html
<!DOCTYPE html>
<html lang="en">
<head>
<meta charset="utf-8">
<title>Harborline Capital Lending – Investor Postcard</title>
<link href="https://fonts.googleapis.com/css2?family=Cabin+Condensed:wght@500&family=Open+Sans:wght@400;600;700&family=Marcellus&display=swap" rel="stylesheet">
<style>
  :root {
    --navy: #16243f;
    --cream: #f3efe6;
    --gold: #c9a14a;
    --gold-light: #e8c874;
    --ink: #2b2b2b;
    --white: #ffffff;
    --backdrop: #a4a4a4;
  }
  * { margin: 0; padding: 0; box-sizing: border-box; }
  html, body { width: 1200px; height: 998px; overflow: hidden; }
  body { background: var(--backdrop); position: relative; font-family: "Open Sans", sans-serif; }

  .postcard {
    position: absolute;
    left: 270px;
    width: 660px;
    height: 462px;
    background: var(--cream);
    box-shadow: 0 6px 18px rgba(0,0,0,.25);
    overflow: hidden;
  }
  .postcard--front { top: 24px; }
  .postcard--back { top: 512px; }
  .postcard svg.shapes { position: absolute; inset: 0; }

  /* front */
  .quote {
    position: absolute; left: 350px; width: 292px; top: 18px;
    font-family: "Cabin Condensed", sans-serif; font-weight: 500;
    color: var(--white); font-size: 25px; line-height: 1.2; text-align: center;
  }
  .quote cite { display: block; font-style: normal; font-size: 20px; margin-top: 6px; }
  .invite {
    position: absolute; left: 356px; width: 282px; top: 170px;
    color: var(--ink); font-size: 13.2px; line-height: 1.42; text-align: center;
  }
  .brand {
    position: absolute; display: flex; align-items: center; gap: 8px;
    font-family: "Open Sans", sans-serif; font-weight: 700; color: var(--navy);
  }
  .brand__dot { width: 18px; height: 18px; border-radius: 50%; background: var(--gold); flex: none; }
  .postcard--front .brand { left: 400px; top: 398px; font-size: 15px; line-height: 1.2; }
  .call {
    position: absolute; left: 0; width: 290px; top: 350px;
    font-family: "Marcellus", serif; color: var(--white); text-align: center;
    font-size: 17px; line-height: 1.3; letter-spacing: .3px;
  }

  /* back */
  .details {
    position: absolute; left: 22px; width: 250px; top: 20px;
    color: var(--white); font-size: 10px; line-height: 1.32;
  }
  .details .hl { color: var(--gold-light); font-weight: 600; }
  .details ul { margin: 8px 0 10px 14px; }
  .details li { margin-bottom: 1px; }
  .details .company { color: var(--gold-light); font-weight: 700; font-size: 13px; margin-bottom: 2px; }
  .details .licence { font-size: 9.8px; }
  .postcard--back .brand { left: 345px; top: 46px; font-size: 12px; width: 180px; line-height: 1.2; }
  .postcard--back .brand__dot { width: 14px; height: 14px; }
  .stamp-box {
    position: absolute; left: 555px; top: 36px; width: 78px; height: 72px;
    border: 2px solid var(--ink);
  }
  .address-line {
    position: absolute; left: 360px; width: 275px; height: 1px; background: var(--ink);
  }
</style>
</head>
<body>

<section class="postcard postcard--front">
  <svg class="shapes" viewBox="0 0 660 462" width="660" height="462">
    <defs>
      <linearGradient id="goldFront" x1="0" y1="0" x2="1" y2="1">
        <stop offset="0" stop-color="#b0802e"/><stop offset=".5" stop-color="#f0d488"/><stop offset="1" stop-color="#a8772a"/>
      </linearGradient>
      <linearGradient id="photoTone" x1="0" y1="0" x2="1" y2="1">
        <stop offset="0" stop-color="#6f8a3c"/><stop offset=".45" stop-color="#c9bda4"/><stop offset="1" stop-color="#8e9a5c"/>
      </linearGradient>
      <clipPath id="leftPanel"><path d="M0,0 H330 C322,150 318,300 290,462 H0 Z"/></clipPath>
    </defs>
    <rect x="0" y="0" width="660" height="146" fill="var(--navy)"/>
    <rect x="0" y="146" width="660" height="4" fill="url(#goldFront)"/>
    <g clip-path="url(#leftPanel)">
      <rect x="0" y="0" width="340" height="332" fill="url(#photoTone)" role="img" aria-label="Photo of a smiling senior couple sitting together outdoors in a green park"/>
      <rect x="0" y="332" width="340" height="4" fill="url(#goldFront)"/>
      <rect x="0" y="336" width="340" height="126" fill="var(--navy)"/>
    </g>
    <path d="M330,0 C322,150 318,300 290,462" fill="none" stroke="url(#goldFront)" stroke-width="4"/>
  </svg>

  <blockquote class="quote">
    “He who earns and does not invest will have to work for the rest of his life.”
    <cite>-Arlen Voss</cite>
  </blockquote>

  <p class="invite">As an experienced or recent California trust deed investor I would like to invite you to join our email list to receive our trust deed investment Executive Summaries. These one-page summaries are emailed when newly originated trust deed investments are ready for review and funding. Harborline Capital Lending, Inc. has been originating privately funded or “hard money” loans in California since 2001.</p>

  <div class="brand"><span class="brand__dot"></span><span>Harborline Capital<br>Lending, Inc.</span></div>

  <div class="call">CALL:<br>1-800-555-0147<br>WWW.HARBORLINELENDING.INFO</div>
</section>

<section class="postcard postcard--back">
  <svg class="shapes" viewBox="0 0 660 462" width="660" height="462">
    <defs>
      <linearGradient id="goldBack" x1="0" y1="0" x2="1" y2="1">
        <stop offset="0" stop-color="#b0802e"/><stop offset=".5" stop-color="#f0d488"/><stop offset="1" stop-color="#a8772a"/>
      </linearGradient>
    </defs>
    <path d="M0,0 H360 C305,40 292,300 282,462 H0 Z" fill="var(--navy)"/>
    <path d="M360,0 C305,40 292,300 282,462" fill="none" stroke="url(#goldBack)" stroke-width="4"/>
  </svg>

  <div class="details">
    <p>If the <span class="hl">monthly income</span> offered by <span class="hl">well-secured trust deed investments</span> is attractive to you, please go to our website at: www.harborlinelending.info to subscribe to our email list and learn more about Harborline and trust deed investing. Our telephone number is 1-800-555-0147.</p>
    <ul>
      <li>Complete investor due diligence package.</li>
      <li>Currently originating non-owner occupied residential loans (business purpose).</li>
      <li>Loan documents including note and deed of trust show your name and vesting.</li>
      <li>Fund directly to the insuring title company.</li>
      <li>Utilizing leading industry loan and lender document packages.</li>
      <li>Typical terms are for 3-7 years.</li>
      <li>Both purchase and refinance loans.</li>
    </ul>
    <p class="company">Harborline Capital Lending, Inc.</p>
    <p class="licence">1480 Canyon View Road, Suite 210<br>Palm Springs CA 92262<br>
    <strong>Call: (800) 555-0147</strong><br>
    CA Department of Real Estate<br>
    Real Estate Broker License # 02457719<br>NMLS # 418305<br>
    Daniel Mercer CA Department of Real Estate –<br>
    Real Estate Broker License # 01984436<br>NMLS # 571690</p>
  </div>

  <div class="brand"><span class="brand__dot"></span><span>Harborline Capital<br>Lending, Inc.</span></div>
  <div class="stamp-box"></div>
  <div class="address-line" style="top:318px"></div>
  <div class="address-line" style="top:356px"></div>
  <div class="address-line" style="top:394px"></div>
</section>

</body>
</html>
```